BRISK SWEEP

Need a professional looking business card that can fit : Name, Title, Cell, and office phone numbers. On the flip side we would like a list of our services : Highway accident management and towing, Crime scene clean up, Illegal drug lab clean up, Drug disposal, and Hazardous materials clean up.

```html
<!DOCTYPE html>
<html lang="en">
<head>
<meta charset="utf-8">
<title>Brisk Sweep Business Card</title>
<link href="https://fonts.googleapis.com/css2?family=Caladea:wght@400;700&display=swap" rel="stylesheet">
<style>
  :root {
    --backdrop: #e9e6e1;
    --card-white: #ffffff;
    --navy: #10365a;
    --navy-deep: #0c2a47;
    --gold: #e0b720;
    --name-gold: #d9ac1e;
    --ink: #1b1b1b;
    --list-ink: #07192b;
    --faint: rgba(16, 54, 90, 0.07);
    --faint-on-navy: rgba(255, 255, 255, 0.05);
  }
  * { margin: 0; padding: 0; box-sizing: border-box; }
  html, body {
    width: 1200px; height: 1023px; overflow: hidden;
    background: var(--backdrop);
    font-family: "Caladea", Cambria, Georgia, serif;
  }
  .canvas { position: relative; width: 1200px; height: 1023px; }

  .card {
    position: absolute; width: 700px; height: 400px; left: 250px;
    box-shadow: 0 6px 18px rgba(0,0,0,0.18);
    overflow: hidden;
  }

  /* Front */
  .card-front { top: 62px; background: var(--card-white); }
  .card-front .accent-band {
    position: absolute; left: 0; right: 0; bottom: 0; height: 22px; background: var(--gold);
  }
  .card-front .watermark {
    position: absolute; left: 330px; top: 40px;
    font-size: 58px; font-weight: 700; color: var(--faint); letter-spacing: 2px;
  }
  .brand {
    position: absolute; left: 40px; top: 150px;
    display: flex; align-items: center; gap: 12px;
  }
  .brand-dot { width: 34px; height: 34px; border-radius: 50%; background: var(--navy); }
  .brand-name { font-size: 26px; font-weight: 700; color: var(--navy); letter-spacing: 1px; }

  .person { position: absolute; left: 215px; top: 215px; }
  .person-line { display: flex; align-items: baseline; gap: 8px; }
  .person-name { font-size: 38px; color: var(--name-gold); }
  .person-divider { font-size: 30px; color: var(--ink); }
  .person-title { font-size: 28px; font-weight: 700; color: var(--ink); }

  .contacts { list-style: none; margin-top: 10px; margin-left: 4px; }
  .contacts li {
    display: flex; align-items: center; gap: 14px;
    font-size: 20px; color: var(--ink); line-height: 31px;
  }
  .contacts svg { width: 18px; height: 18px; flex: none; }

  /* Back */
  .card-back { top: 540px; background: var(--navy); }
  .card-back .tab {
    position: absolute; right: 0; top: 0; width: 20px; height: 290px; background: var(--gold);
  }
  .card-back .watermark {
    position: absolute; left: 250px; top: 140px;
    font-size: 64px; font-weight: 700; color: var(--faint-on-navy); letter-spacing: 2px;
  }
  .services { position: absolute; left: 52px; top: 96px; }
  .services-heading { font-size: 26px; font-weight: 700; color: #ffffff; margin-bottom: 10px; }
  .services-list { list-style: none; }
  .services-list li {
    display: flex; align-items: center; gap: 16px;
    font-size: 22px; color: var(--list-ink); line-height: 36px;
  }
  .services-list li::before {
    content: "\2605"; color: var(--gold); font-size: 20px;
  }
</style>
</head>
<body>
<div class="canvas">

  <section class="card card-front">
    <div class="watermark" aria-hidden="true">BRISK SWEEP</div>
    <div class="brand">
      <span class="brand-dot"></span>
      <span class="brand-name">BRISK SWEEP</span>
    </div>
    <div class="person">
      <div class="person-line">
        <span class="person-name">Your Name</span>
        <span class="person-divider">|</span>
        <span class="person-title">CEO</span>
      </div>
      <ul class="contacts">
        <li>
          <svg viewBox="0 0 18 18" aria-hidden="true"><rect x="4" y="1" width="10" height="16" rx="2" fill="none" stroke="#1b1b1b" stroke-width="1.6"/><circle cx="9" cy="14" r="1" fill="#1b1b1b"/></svg>
          12345 678910
        </li>
        <li>
          <svg viewBox="0 0 18 18" aria-hidden="true"><path d="M4 2l3 3-2 2c1 2 3 4 5 5l2-2 3 3-2 3C7 16 2 11 1 4z" fill="none" stroke="#1b1b1b" stroke-width="1.6" stroke-linejoin="round"/></svg>
          12345 678910
        </li>
        <li>
          <svg viewBox="0 0 18 18" aria-hidden="true"><rect x="1" y="4" width="16" height="11" fill="#1b1b1b"/><path d="M1 4l8 6 8-6" fill="none" stroke="#ffffff" stroke-width="1.4"/></svg>
          your@brisksweep.com
        </li>
      </ul>
    </div>
    <div class="accent-band"></div>
  </section>

  <section class="card card-back">
    <div class="watermark" aria-hidden="true">BRISK SWEEP</div>
    <div class="tab"></div>
    <div class="services">
      <h2 class="services-heading">Our services :</h2>
      <ul class="services-list">
        <li>Highway accident management and towing,</li>
        <li>Crime scene clean up,</li>
        <li>Illegal drug lab clean up,</li>
        <li>Drug disposal, and</li>
        <li>Hazardous materials clean up</li>
      </ul>
    </div>
  </section>

</div>
</body>
</html>
```